Velmar Ops Business Cards

We need to design some upbeat business cards. We are an Industrial Rope Access Company/Height Safety Company that specialize in Rope Access, Confined Space, Anchor Points, Safety Systems, PPE Inspecions and Rigging.
Company name is Velmar Ops Ltd
Card is for Gareth Lomas the Company Director
His mobile number is 027 418 9072 and email is gareth@velmarops.co.nz. Website address is www.velmarops.co.nz.
We will post some pictures below to ensure you get a good idea of what we do.

```html
<!DOCTYPE html>
<html lang="en">
<head>
<meta charset="utf-8">
<title>Velmar Ops Ltd – Business Cards</title>
<link href="https://fonts.googleapis.com/css2?family=Roboto+Condensed:wght@400;700&family=Roboto:wght@400&display=swap" rel="stylesheet">
<style>
  :root {
    --card-blue: #364498;
    --accent-cyan: #2bb5e0;
    --rule-black: #050505;
    --text-white: #ffffff;
    --text-soft: #d9dcec;
    --stage-light: #ffffff;
    --stage-dark: #6a6a6a;
  }
  * { margin: 0; padding: 0; box-sizing: border-box; }
  html, body { width: 1200px; height: 1200px; overflow: hidden; }
  body {
    position: relative;
    background: radial-gradient(ellipse at 50% 50%, var(--stage-light) 0%, #c9c9c9 35%, var(--stage-dark) 100%);
    font-family: "Roboto Condensed", sans-serif;
  }
  .card {
    position: absolute;
    background: var(--card-blue);
    border-radius: 48px;
  }
  .card--front { left: 186px; top: 68px; width: 827px; height: 480px; }
  .card--back  { left: 198px; top: 630px; width: 828px; height: 468px; }
  .card svg { position: absolute; left: 0; top: 0; }

  .company-name {
    position: absolute;
    color: var(--text-white);
    font-family: "Roboto Condensed", sans-serif;
    font-weight: 700;
    white-space: nowrap;
  }
  .card--front .company-name {
    left: 0; width: 100%; top: 86px; text-align: center;
    font-size: 62px; line-height: 1;
  }
  .front-url {
    position: absolute; left: 0; width: 100%; top: 188px; text-align: center;
    color: var(--text-white); font-size: 36px; line-height: 1;
    text-shadow: 0 2px 4px rgba(0,0,0,0.45);
  }
  .card--back .company-name {
    left: 32px; top: 48px; font-size: 38px; line-height: 1;
  }
  .holder-name {
    position: absolute; left: 144px; width: 280px; top: 184px; text-align: center;
    color: var(--text-white); font-weight: 700; font-size: 32px; letter-spacing: 2px; line-height: 1;
  }
  .holder-role {
    position: absolute; left: 144px; width: 280px; top: 236px; text-align: center;
    color: var(--text-white); font-size: 23px; line-height: 1;
  }
  .contact {
    position: absolute; font-family: "Roboto", sans-serif;
    color: var(--text-soft); font-size: 20px; line-height: 25px;
  }
  .contact--phone { left: 506px; top: 236px; }
  .contact--online { left: 502px; top: 292px; }
</style>
</head>
<body>

  <section class="card card--front">
    <div class="company-name">Velmar Ops Ltd</div>
    <div class="front-url">www.velmarops.co.nz</div>
    <svg width="827" height="480" aria-hidden="true">
      <g stroke="var(--rule-black)" stroke-width="3.5">
        <line x1="111" y1="253" x2="732" y2="253"/>
        <line x1="111" y1="273" x2="732" y2="273"/>
        <line x1="111" y1="292" x2="732" y2="292"/>
      </g>
    </svg>
  </section>

  <section class="card card--back">
    <svg width="828" height="468" aria-hidden="true">
      <g stroke="var(--accent-cyan)" fill="none">
        <line x1="268" y1="102" x2="740" y2="100" stroke-width="3"/>
        <line x1="144" y1="227" x2="420" y2="227" stroke-width="3"/>
        <line x1="420" y1="172" x2="420" y2="340" stroke-width="3"/>
        <rect x="423" y="228" width="53" height="44" stroke-width="1.5"/>
        <rect x="423" y="297" width="53" height="43" stroke-width="1.5"/>
        <!-- phone icon -->
        <rect x="439" y="237" width="20" height="26" rx="4" stroke-width="1.3"/>
        <path d="M444 242c-1 5 2 12 7 15l2-2-3-3-2 1c-2-2-3-5-3-7l2-1-1-4z" stroke-width="1.2"/>
        <!-- globe icon -->
        <circle cx="449" cy="318" r="12" stroke-width="1.3"/>
        <ellipse cx="449" cy="318" rx="5" ry="12" stroke-width="1.1"/>
        <line x1="437" y1="318" x2="461" y2="318" stroke-width="1.1"/>
        <line x1="439" y1="312" x2="459" y2="312" stroke-width="1.1"/>
        <line x1="439" y1="324" x2="459" y2="324" stroke-width="1.1"/>
      </g>
      <g fill="var(--accent-cyan)">
        <circle cx="740" cy="101" r="4.5"/>
        <circle cx="420" cy="173" r="4.5"/>
      </g>
    </svg>
    <div class="company-name">Velmar Ops Ltd</div>
    <div class="holder-name">Gareth Lomas</div>
    <div class="holder-role">Director</div>
    <div class="contact contact--phone">027 418 9072</div>
    <div class="contact contact--online">www.velmarops.co.nz<br>gareth@velmarops.co.nz</div>
  </section>

</body>
</html>
```